New Wipes designs - elegant and nice

3 Variants

1. Baby Wipes - Need optons (Blue and Pink colour for Unisex)
2. Mackup Remover - Pink (or you can advice)
3. Abaya Remover - Black or Purple (or you can advice)

Brief for Baby wipes
- Velour Meadow (logo)
- BABY WIPES (nice baby font)
- Eliminates 99% of germs and bacterias, giving healthy and soft skin

Brief for Makeup Remover
- Velour Meadow (logo)
- Makeup Remover
- Special ultra soft formula which gently cleanses and removes makeup and waterproof mascara for the soft skin.

Brief for Baby wipes
- Velour Meadow (logo)
- Abaya Cleaner
- Dummy copy Dummy copy Dummy copy Dummy copy

Mandatory for all wipes
• dermatology tested icon or word
• ph 5.5
• No Alcohol

Target Market(s)

Arab modern women and Asians

Industry/Entity Type

Baby

Requirements
Must have
• Should be feminine and looks elegant, modern, can add premium baby images/ model face where makeup removal effect and abayas... give little tint of arabic pattern.
Nice to have
• you can advice from your side

```html
<!DOCTYPE html>
<html lang="en">
<head>
<meta charset="utf-8">
<title>Velour Meadow – Abaya Cleaner Wet Towels</title>
<link href="https://fonts.googleapis.com/css2?family=Kaushan+Script&family=Open+Sans:ital,wght@0,600;1,300&family=Oswald:wght@600;700&display=swap" rel="stylesheet">
<style>
  :root {
    --bg-deep: #0d0b14;
    --bg-violet: #2a1c45;
    --band-dark: #16121f;
    --band-mid: #241a36;
    --gold: #d9a43a;
    --gold-dark: #b97a16;
    --script-blue: #5b86d6;
    --script-blue-deep: #2f4ea8;
    --script-shadow: #7a3cbf;
    --purple: #6b2fa3;
    --purple-text: #7b3fc4;
    --copy-grey: #7a7585;
    --white: #ffffff;
  }
  * { margin: 0; padding: 0; box-sizing: border-box; }
  html, body { width: 1200px; height: 704px; overflow: hidden; background: var(--bg-deep); }
  .label {
    position: relative; width: 1200px; height: 704px; overflow: hidden;
    background:
      radial-gradient(ellipse 600px 420px at 900px 380px, rgba(92,60,150,.45), transparent 70%),
      radial-gradient(ellipse 500px 300px at 0 300px, rgba(70,30,90,.5), transparent 70%),
      linear-gradient(180deg, #0b0a10 0%, #14101e 45%, var(--bg-violet) 100%);
  }
  .mandala-art {
    position: absolute; left: 600px; top: 0; width: 600px; height: 600px;
    border-radius: 50%;
    background: radial-gradient(circle at 50% 50%, rgba(110,80,170,.35) 0%, rgba(80,55,130,.25) 45%, rgba(60,40,100,0) 72%);
  }
  .waves { position: absolute; left: 0; top: 0; }
  .brand {
    position: absolute; left: 252px; top: 88px;
    font-family: "Open Sans", sans-serif; font-weight: 600;
    font-size: 38px; color: var(--gold); letter-spacing: .5px;
  }
  .title {
    position: absolute; display: inline-block; white-space: nowrap;
    padding: 20px 60px 40px 20px;
    font-family: "Kaushan Script", cursive; font-weight: 400;
    color: var(--script-blue); line-height: 1; letter-spacing: 5px;
    background: linear-gradient(100deg, #7aa3e8 0%, var(--script-blue) 45%, var(--script-blue-deep) 100%);
    -webkit-background-clip: text; background-clip: text; -webkit-text-fill-color: transparent;
    filter: drop-shadow(5px 5px 0 var(--script-shadow));
  }
  .title--abaya { left: 160px; top: 150px; font-size: 166px; }
  .title--cleaner { left: 124px; top: 304px; font-size: 156px; }
  .ribbon { position: absolute; left: 422px; top: 500px; width: 244px; height: 46px; }
  .ribbon-text {
    position: absolute; left: 422px; top: 500px; width: 244px; height: 46px;
    display: flex; align-items: center; justify-content: center;
    font-family: "Kaushan Script", cursive; font-size: 30px; color: var(--white);
  }
  .body-copy {
    position: absolute; left: 166px; top: 584px; width: 416px; text-align: center;
    font-family: "Open Sans", sans-serif; font-style: italic; font-weight: 300;
    font-size: 22px; line-height: 29px; color: var(--copy-grey);
  }
  .ph-badge {
    position: absolute; left: 46px; top: 590px; width: 72px; height: 72px; border-radius: 50%;
    background: var(--purple); color: var(--white);
    display: flex; flex-direction: column; align-items: center; justify-content: center;
    font-family: "Oswald", sans-serif; font-weight: 600; font-size: 21px; line-height: 22px;
  }
  .derm-badge { position: absolute; left: 1034px; top: 498px; }
  .derm-label {
    font-family: "Oswald", sans-serif; font-weight: 700; font-size: 7px; fill: var(--white);
  }
  .count {
    position: absolute; left: 970px; top: 584px; width: 190px; text-align: center;
    font-family: "Oswald", sans-serif; font-weight: 700; color: var(--purple-text); line-height: 1;
  }
  .count-number { display: block; font-size: 40px; }
  .count-unit { display: block; font-size: 34px; margin-top: 2px; }
</style>
</head>
<body>
<main class="label">
  <div class="mandala-art" role="img" aria-label="Faint decorative Arabic-style mandala pattern"></div>

  <svg class="waves" width="1200" height="704" viewBox="0 0 1200 704" aria-hidden="true">
    <path d="M0 360 C150 420 260 520 420 560 C620 610 820 560 1200 540 L1200 704 L0 704 Z" fill="#1d1530" opacity=".8"/>
    <path d="M0 600 C200 640 400 640 620 600 C820 560 980 560 1200 580 L1200 704 L0 704 Z" fill="var(--band-mid)"/>
    <path d="M0 640 C220 690 420 690 640 660 C840 632 1000 650 1200 680 L1200 704 L0 704 Z" fill="var(--band-dark)"/>
  </svg>

  <div class="brand">Velour Meadow</div>

  <h1 class="title title--abaya">Abaya</h1>
  <h1 class="title title--cleaner">Cleaner</h1>

  <svg class="ribbon" viewBox="0 0 244 46" aria-hidden="true">
    <defs>
      <linearGradient id="ribbonGold" x1="0" x2="1">
        <stop offset="0" stop-color="#e9a92c"/>
        <stop offset=".5" stop-color="#f3b640"/>
        <stop offset="1" stop-color="#d98b1a"/>
      </linearGradient>
    </defs>
    <polygon points="0,4 244,0 230,23 244,46 10,42 22,24" fill="url(#ribbonGold)"/>
  </svg>
  <div class="ribbon-text">Quickly Clean</div>

  <p class="body-copy">Dummy copy Dummy copy Dummy copy<br>Dummy copy</p>

  <div class="ph-badge"><span>PH</span><span>5.5</span></div>

  <svg class="derm-badge" width="60" height="74" viewBox="0 0 60 74" role="img" aria-label="Dermatology tested">
    <defs>
      <linearGradient id="dropGold" x1="0" y1="0" x2="0" y2="1">
        <stop offset="0" stop-color="#f2b640"/>
        <stop offset="1" stop-color="var(--gold-dark)"/>
      </linearGradient>
    </defs>
    <path d="M28 6 C34 20 56 34 56 50 A26 24 0 0 1 4 50 C4 34 22 20 28 6 Z" fill="url(#dropGold)"/>
    <path d="M14 30 L24 42 L56 4" fill="none" stroke="var(--purple)" stroke-width="5" stroke-linecap="round" stroke-linejoin="round"/>
    <text class="derm-label" x="30" y="55" text-anchor="middle">DERMATOLOGY</text>
    <text class="derm-label" x="30" y="64" text-anchor="middle">TESTED</text>
  </svg>

  <div class="count">
    <span class="count-number">12</span>
    <span class="count-unit">Wet Towels</span>
  </div>
</main>
</body>
</html>
```